Business Card for Quillmark Ledger - A cannabis publication for executives.

I'd like some business cards for Quillmark Ledger. The logo is done (great job!) and I need a card design I will use with PRINTLY. I made it a short project to allow time for printing before an event. These will be standard sized cards (final artwork size 3.66" x 2.16" at 300dpi) with a final card size of 3.5" x 2.0". (See PRINTLY.com if you need more info.) I might try rounded corners but am not sure yet. I think the design will work okay with rounded.

Quillmark Ledger will be a bi-weekly publication for the cannabis industry. It is targeted to investors and industry executives, not consumers or pot smokers. So our market is more B2B. However I am open to creativity and making the card something people remark on.

My contact for card:

Dana Merrow
Founder/CEO
dana@quillmarkledger.example

2740 Harlow Avenue
Boston MA 02135
(617)555-0194

Target Market(s)

Executives, Industry people and investors in the Cannabis sector.

Contact Information for Business Card

PRINTLY does do double sided and the second side can be the same or different images. Only one side is required but use of the second side would be a bonus.

Font styles to use
Serif
Sans Serif
Decorative

Colors

Designer to choose colors to be used in the design.

Requirements
Must have
• Logo, contact info
Nice to have
• Style and design to make the card stand out in a crowd.

```html
<!DOCTYPE html>
<html lang="en">
<head>
<meta charset="utf-8">
<title>Quillmark Ledger Business Cards</title>
<link rel="stylesheet" href="https://fonts.googleapis.com/css2?family=Arvo:ital,wght@1,700&family=Source+Sans+3:wght@400;600;700&display=swap">
<style>
  :root {
    --blue: #1a75bc;
    --green: #80ad35;
    --green-line: #8cb234;
    --white: #ffffff;
    --ink: #111111;
    --paper: #ffffff;
  }
  * { box-sizing: border-box; margin: 0; padding: 0; }
  html, body { width: 849px; height: 1200px; overflow: hidden; background: var(--paper); }
  body { position: relative; font-family: "Source Sans 3", Arial, sans-serif; }

  .card {
    position: absolute;
    width: 361px;
    height: 202px;
  }
  .card--front { left: 54px; border-radius: 6px 52px 6px 52px; }
  .card--back  { left: 441px; border-radius: 52px 6px 52px 6px; }
  .card__frame {
    position: absolute;
    inset: 10px;
    border: 1.5px solid var(--frame);
  }
  .card--front .card__frame { border-radius: 4px 42px 4px 42px; }
  .card--back .card__frame  { border-radius: 42px 4px 42px 4px; }

  .row--white { top: 81px; }
  .row--blue  { top: 317px; }
  .row--green { top: 603px; }

  .theme-white { background: var(--white); border: 1px solid var(--ink); --frame: var(--green-line); --name: var(--blue); --icon: var(--blue); --text: var(--ink); --brand: var(--green); }
  .theme-blue  { background: var(--blue); --frame: var(--green-line); --name: var(--green-line); --icon: var(--green-line); --text: var(--white); --brand: var(--white); }
  .theme-green { background: var(--green); --frame: var(--blue); --name: var(--blue); --icon: var(--blue); --text: var(--white); --brand: var(--white); }

  .brand {
    position: absolute;
    left: 0; right: 0; top: 50%;
    transform: translateY(-50%);
    display: flex;
    align-items: center;
    justify-content: center;
    gap: 10px;
    color: var(--brand);
    font-weight: 700;
    font-size: 29px;
    letter-spacing: -0.3px;
  }
  .brand__mark {
    width: 30px; height: 30px;
    border-radius: 50%;
    background: var(--brand);
  }

  .person {
    position: absolute;
    right: 21px;
    top: 18px;
    text-align: right;
  }
  .person__name {
    font-family: "Arvo", Georgia, serif;
    font-style: italic;
    font-weight: 700;
    font-size: 16px;
    color: var(--name);
    line-height: 1.1;
  }
  .person__role {
    font-size: 11.5px;
    color: var(--text);
    line-height: 1.3;
  }

  .contact {
    position: absolute;
    left: 24px;
    top: 125px;
    list-style: none;
  }
  .contact__item {
    display: flex;
    align-items: center;
    gap: 6px;
    height: 20px;
    font-size: 10.5px;
    font-weight: 700;
    color: var(--text);
  }
  .contact__icon { width: 12px; height: 12px; fill: var(--icon); flex: none; }
</style>
</head>
<body>
<svg width="0" height="0" style="position:absolute">
  <defs>
    <symbol id="icon-mail" viewBox="0 0 12 12"><path d="M0 2.5h12v7H0z"/><path d="M0.5 3l5.5 3.6L11.5 3" fill="none" stroke="#fff" stroke-width="0.9"/></symbol>
    <symbol id="icon-phone" viewBox="0 0 12 12"><path d="M2.6 1l2 2.4-1.2 1.3c.8 1.6 2 2.8 3.4 3.6l1.3-1.2L11 9.2 9.5 11C5 10.6 1.3 6.9 1 2.4z"/></symbol>
    <symbol id="icon-home" viewBox="0 0 12 12"><path d="M6 1L0.5 6h1.7v5h3V8h1.6v3h3V6h1.7z"/></symbol>
  </defs>
</svg>

<!-- White set -->
<section class="card card--front row--white theme-white">
  <div class="card__frame"></div>
  <div class="brand"><span class="brand__mark"></span>Quillmark Ledger</div>
</section>
<section class="card card--back row--white theme-white">
  <div class="card__frame"></div>
  <div class="person"><p class="person__name">Dana Merrow</p><p class="person__role">Founder/CEO</p></div>
  <ul class="contact">
    <li class="contact__item"><svg class="contact__icon"><use href="#icon-mail"/></svg>dana@quillmarkledger.example</li>
    <li class="contact__item"><svg class="contact__icon"><use href="#icon-phone"/></svg>(617)555-0194</li>
    <li class="contact__item"><svg class="contact__icon"><use href="#icon-home"/></svg>2740 Harlow Avenue, Boston MA 02135</li>
  </ul>
</section>

<!-- Blue set -->
<section class="card card--front row--blue theme-blue">
  <div class="card__frame"></div>
  <div class="brand"><span class="brand__mark"></span>Quillmark Ledger</div>
</section>
<section class="card card--back row--blue theme-blue">
  <div class="card__frame"></div>
  <div class="person"><p class="person__name">Dana Merrow</p><p class="person__role">Founder/CEO</p></div>
  <ul class="contact">
    <li class="contact__item"><svg class="contact__icon"><use href="#icon-mail"/></svg>dana@quillmarkledger.example</li>
    <li class="contact__item"><svg class="contact__icon"><use href="#icon-phone"/></svg>(617)555-0194</li>
    <li class="contact__item"><svg class="contact__icon"><use href="#icon-home"/></svg>2740 Harlow Avenue, Boston MA 02135</li>
  </ul>
</section>

<!-- Green set -->
<section class="card card--front row--green theme-green">
  <div class="card__frame"></div>
  <div class="brand"><span class="brand__mark"></span>Quillmark Ledger</div>
</section>
<section class="card card--back row--green theme-green">
  <div class="card__frame"></div>
  <div class="person"><p class="person__name">Dana Merrow</p><p class="person__role">Founder/CEO</p></div>
  <ul class="contact">
    <li class="contact__item"><svg class="contact__icon"><use href="#icon-mail"/></svg>dana@quillmarkledger.example</li>
    <li class="contact__item"><svg class="contact__icon"><use href="#icon-phone"/></svg>(617)555-0194</li>
    <li class="contact__item"><svg class="contact__icon"><use href="#icon-home"/></svg>2740 Harlow Avenue, Boston MA 02135</li>
  </ul>
</section>
</body>
</html>
```